Holiday Rental Company Flyer Design (DL not A5)

Note from PixelFolk Administration: The category sizing selected is A5, however the project requires DL sized artwork. Please refer to the DL template link below while the 'Special Requirements' are updated accordingly.

Project Brief:
We need a double sided DL flyer designed for an up market Holiday Rental Company that portrays a personalised approach to property management. These are to be used for letter box drops to homes we're specifically targeting so the design should be modern, complimentary colour palette, uncluttered & visually appealing.

Please Download the DL Template from Quillmark here: http://www.quillmark.com.au/qm/ns/propath/UploadResources.aspx?selectedTab=0?pfid=BFB&pf_id=BFB&xnav=easypath-upload-image#Templates

Target Market(s)

Wealthy Home Owners

Industry/Entity Type

It Company

Font styles to use
Other font styles liked:
• Avant Garde Extra Light & Demi

Colors
33b8a4

Requirements
Must have
• DL Flyer sizes (210mm width x 99mm width, plus 3mm bleed)
• Front: Logo, Main Image & Grab
• Back: Contact Details & Brief Description of our business
• Images: Ideally the main image should be the house with the pool but alternatively a lifestyle images could also be used.
Nice to have
• A creative designer!
Should not have
• Clutter & busy designs

```html
<!DOCTYPE html>
<html lang="en">
<head>
<meta charset="utf-8">
<title>Harbourline Stays – DL Flyer</title>
<link rel="stylesheet" href="https://fonts.googleapis.com/css2?family=Questrial&family=Didact+Gothic&display=swap">
<style>
  :root {
    --teal: #13b288;
    --teal-deep: #0fa57d;
    --teal-photo: #3cbf99;
    --white: #ffffff;
    --backdrop: #e9eaeb;
    --night: #2a2c6a;
    --pool: #2f7fe0;
    --warm: #c9954a;
  }
  * { box-sizing: border-box; margin: 0; padding: 0; }
  html, body { width: 1200px; height: 1200px; overflow: hidden; }
  body {
    background: var(--backdrop);
    font-family: "Questrial", "Didact Gothic", sans-serif;
    color: var(--white);
    position: relative;
  }
  .flyer {
    position: absolute;
    top: 133px;
    width: 440px;
    height: 934px;
    background: var(--teal);
    overflow: hidden;
  }
  .flyer--front { left: 110px; }
  .flyer--back { left: 650px; }

  /* Front */
  .brand {
    position: absolute;
    top: 92px; left: 0; right: 0;
    text-align: center;
    font-size: 40px;
    line-height: 1.05;
    letter-spacing: 4px;
    text-transform: uppercase;
  }
  .hero {
    position: absolute;
    top: 300px; left: 0; right: 0;
    height: 290px;
    background: linear-gradient(100deg, var(--warm) 0%, #5b4a5a 30%, var(--night) 55%, #6e6fb8 80%, #d8d8ee 100%);
    border-bottom: 5px solid var(--white);
  }
  .hero::after {
    content: "";
    position: absolute; left: 0; right: 0; bottom: 0; height: 90px;
    background: linear-gradient(180deg, rgba(47,127,224,0) 0%, var(--pool) 60%, #1f5fc0 100%);
  }
  .pattern-field {
    position: absolute;
    top: 595px; left: 0; right: 0; bottom: 0;
    background: var(--teal-deep);
  }
  .tagline {
    position: absolute;
    left: 0; right: 0; bottom: 74px;
    text-align: center;
    font-size: 20px;
    line-height: 1.15;
  }

  /* Back */
  .sea {
    position: absolute;
    top: 0; left: 0; right: 0; height: 250px;
    background: linear-gradient(180deg, #28b48d 0%, var(--teal-photo) 60%, #1aae86 100%);
  }
  .back-pattern {
    position: absolute;
    top: 250px; left: 0; width: 205px; bottom: 0;
    background: var(--teal-deep);
  }
  .gallery {
    position: absolute;
    top: 240px; left: 30px; width: 170px;
    display: flex; flex-direction: column; gap: 5px;
  }
  .gallery__shot { height: 122px; }
  .gallery__shot--vase { background: linear-gradient(120deg, #7b6a5c, #b59a80 55%, #b0533a); }
  .gallery__shot--bed { background: linear-gradient(135deg, #e7d8c0, #d8c33a 50%, #e06a5a); }
  .gallery__shot--basin { background: linear-gradient(135deg, #c9ccc9, #eeeeec 60%, #b9bcbb); }
  .divider {
    position: absolute;
    top: 240px; left: 200px; width: 5px; height: 376px;
    background: var(--white);
  }
  .copy {
    position: absolute;
    top: 248px; left: 216px; right: 8px;
    font-family: "Didact Gothic", "Questrial", sans-serif;
    font-size: 11.5px;
    line-height: 1.45;
    white-space: nowrap;
  }
  .copy__title {
    font-family: "Questrial", sans-serif;
    font-size: 14px;
    font-weight: 700;
    margin-bottom: 14px;
  }
  .copy p { margin-bottom: 16px; }
  .copy .enquiry { margin-top: 36px; }
  .copy .contact { font-weight: 700; margin-top: 26px; margin-bottom: 16px; }
  .copy .address { font-weight: 700; }
</style>
</head>
<body>
  <section class="flyer flyer--front" aria-label="Flyer front">
    <div class="brand">Harbourline<br>Stays</div>
    <div class="hero" role="img" aria-label="Modern house at dusk with a lit lap pool"></div>
    <div class="pattern-field" role="img" aria-label="Subtle tonal geometric pattern"></div>
    <p class="tagline">Holiday Rental Management<br>with a difference</p>
  </section>

  <section class="flyer flyer--back" aria-label="Flyer back">
    <div class="sea" role="img" aria-label="Sailing boat on calm water, tinted green"></div>
    <div class="back-pattern" role="img" aria-label="Subtle tonal geometric pattern"></div>
    <div class="gallery">
      <div class="gallery__shot gallery__shot--vase" role="img" aria-label="Interior with flowers in a glass vase"></div>
      <div class="gallery__shot gallery__shot--bed" role="img" aria-label="Bed with yellow cushions and colourful quilt"></div>
      <div class="gallery__shot gallery__shot--basin" role="img" aria-label="Bathroom basin with tiled wall"></div>
    </div>
    <div class="divider"></div>
    <div class="copy">
      <h2 class="copy__title">What we do differently!</h2>
      <p>Rather than relying upon a key safe<br>or a central pick-up destination,<br>a ‘Harbourline Stays’ staff member<br>will greet guests upon arrival.</p>
      <p>Our ‘Meet &amp; Greet’ service<br>provides home owners<br>with an increased level<br>of Security and also allows us to:</p>
      <p>Prepare the home for their arrival<br>(lights, heaters, music etc.)<br>Establish a rapport &amp; help<br>facilitate future bookings<br>Reiterate their responsibilities<br>to ensure the return of their bond</p>
      <p class="enquiry">If you’d like to know<br>what your property could achieve<br>or require additional information,<br>please contact us on:</p>
      <p class="contact">t: (03)5900 1234<br>e: stay@harbourlinestays.com.au<br>w: harbourlinestays.com.au</p>
      <p class="address">PO Box 12, Seacliff Victoria 3990</p>
    </div>
  </section>
</body>
</html>
```